Accountant website

Please design a accountant website for www.fenwaylodgeadvisory.com.au. This site is majorly out of date, and is not supported by modern browsers.

The style should use the reds from the design at dev.fenwaylodgeadvisory.com.au, and should be modern and make use of Slides (large content slides that the user scrolls through on the front page).

The content is largely already on the site, however happy to move some around to suit the modern design as required.

The dev.fenwaylodgeadvisory.com.au was a rough mock up that I have completed that the client is "happy" with the direction, however this needs a lot of polish and finishing touches, and I will accept designs that differ from this, but highly recommend that this is used as a guide.

Ready to be sliced PSD Only - HTML no required.

In all honesty, although I can technically do a lot of this, the polished finished I want for this site has eluded me in a few attempts, and therefore I am looking out there at you much more artistic people to finish (or redesign if required) this site.

Target Market(s)

Higher end Small - Medium Business

Industry/Entity Type

Accountant

Requirements
Must have
• Must use the logo from dev.fenwaylodgeadvisory.com.au use exactly the red colours as defined in this layout. A basic layout PSD (to get the colour etc) and the logo in ai format is attached to this project. Please ignore the SSL warning on the development site.

The final product does NOT have to be the same as shown on dev.fenwaylodgeadvisory.com.au however the red colour scheme must be used. The client DOES want the logo on the RIGHT.

Must have a front landing page design, and a page layout that considers the other page content (at least one separate PSD)
Nice to have
• I really am looking at a slide format for the front page simular to:

http://www.plumvine.com/au/
http://www.tidelockbox.com/

The attached photos should be used on the site. Was considering a rotating banner with these images are a watermark background on a solid Red header bar, but happy to be shown other options.
Should not have
• Please no "Pattern Goblin" submissions.

```html
<!DOCTYPE html>
<html lang="en">
<head>
<meta charset="utf-8">
<title>Fenway Lodge Advisory</title>
<link rel="stylesheet" href="https://fonts.googleapis.com/css2?family=PT+Sans:wght@400;700&family=Rokkitt:wght@400&family=Arimo:wght@400;700&display=swap">
<style>
:root{
  --red:#c8252b;
  --ink:#2b2b2b;
  --body:#444;
  --muted:#777;
  --band:#efefef;
  --line:#dcdcdc;
  --black:#000;
  --footer:#1f1f1f;
  --footer-text:#e6e6e6;
  --gold:#d8a43a;
  --yellow:#f6b800;
  --orange:#e08a12;
}
*{box-sizing:border-box;margin:0;padding:0}
html,body{width:782px;height:1200px;overflow:hidden}
body{position:relative;background:#fff;font-family:Arimo,Arial,sans-serif;color:var(--body)}
.abs{position:absolute}

/* header */
.site-header{left:0;top:0;width:782px;height:84px;background:linear-gradient(#fafafa,#f0f0f0);border-bottom:3px solid var(--line)}
.brand{right:67px;top:18px;display:flex;align-items:center;gap:8px}
.brand-name{font-family:"PT Sans",sans-serif;font-weight:700;color:var(--ink);font-size:22px;line-height:24px;letter-spacing:.5px;text-align:right}
.brand-name small{display:block;font-size:10px;line-height:12px;font-weight:700;letter-spacing:.3px}
.brand-mark{width:14px;height:14px;background:var(--red)}
.login{left:67px;top:8px;display:flex;gap:8px;align-items:center;font-size:9px;color:var(--muted)}
.login .field{width:64px;height:16px;border-radius:8px;background:#fff;border:1px solid #e2e2e2}
.login .go{width:20px;height:16px;border-radius:5px;background:var(--red)}
.main-nav{left:67px;top:58px;display:flex;font-size:9px;color:#333}
.main-nav span{display:flex;align-items:center}
.main-nav span+span::before{content:"";width:5px;height:5px;border-top:2px solid var(--red);border-right:2px solid var(--red);transform:rotate(45deg);margin:0 10px 0 8px}
.main-nav .current{border-bottom:2px solid var(--red);padding:0 3px 7px}

/* hero slider */
.hero{left:0;top:91px;width:782px;height:322px;background:var(--black)}
.hero-frame{left:71px;top:19px;width:641px;height:286px;background:#fff}
.hero-photo{left:7px;top:8px;width:627px;height:270px;background:linear-gradient(100deg,#8a9aa8 0%,#b9c2c8 35%,#a5593f 55%,#b2232b 68%,#c9c6bd 85%,#7f9270 100%)}
.hero-arrow{top:144px;width:33px;height:28px;background:#1b1b1b;display:flex;align-items:center;justify-content:center}
.hero-arrow.prev{left:62px;border-radius:0 14px 14px 0}
.hero-arrow.next{left:687px;border-radius:14px 0 0 14px}

/* intro */
h2{font-family:"PT Sans",sans-serif;font-weight:400;color:var(--ink);font-size:17px}
.intro{left:72px;top:443px;width:340px;font-size:9.5px;line-height:14.5px}
.intro .lead{font-weight:700;margin:20px 0 14px}
.why{left:441px;top:440px;width:278px}
.why-rule{left:0;top:27px;width:208px;height:1px;background:var(--line)}
.why-pager{left:215px;top:21px;display:flex;gap:4px}
.why-pager span{width:15px;height:15px;background:#ececec;font-size:10px;text-align:center;line-height:15px;color:#333}
.post-date{left:2px;top:41px;width:42px;height:46px;background:#3a3a3a;border:1px solid #666;color:#fff;text-align:center;font-family:Rokkitt,serif}
.post-date b{display:block;font-weight:400;font-size:18px;line-height:22px;margin-top:3px}
.post-date i{display:block;font-style:normal;font-size:6px;line-height:8px;color:#bbb}
.post-title{left:52px;top:40px;width:230px;font-family:Rokkitt,serif;color:var(--red);font-size:14px;line-height:17px}
.post-meta{left:52px;top:80px;font-size:6px;color:#666}
.post-text{left:3px;top:94px;width:280px;font-size:9.5px;line-height:14.5px}

/* team band */
.team{left:0;top:604px;width:782px;height:231px;background:var(--band)}
.portrait{width:175px;height:175px;border-radius:50%;background:radial-gradient(circle at 50% 40%,#d9b39c 0,#a78670 28%,#8ea4b5 55%,#b7c5cf 100%)}
.badge{width:92px;height:92px;border-radius:50%;background:#fff;border:3px solid #f2f2f2;text-align:center;padding-top:20px}
.badge h3{font-family:"PT Sans",sans-serif;font-weight:400;font-size:10.5px;color:#222}
.badge p{font-size:6px;line-height:10px;color:#666;padding:2px 11px 0}
.badge.featured{background:var(--yellow);border-color:#ffd23d}
.badge.featured h3,.badge.featured p{color:#fff}
.dots{left:368px;top:813px;display:flex;gap:4px}
.dots span{width:17px;height:17px;border-radius:50%;border:1.5px solid #777;background:#f7f7f7}

/* lower */
.tips{left:72px;top:858px;width:308px}
.quote{left:0;top:29px;width:306px;height:60px;background:#f1f1f1;border:1px solid #ddd;padding:9px 10px 0 34px;font-family:"PT Sans",sans-serif;font-style:italic;font-size:8.5px;line-height:13px;color:#777}
.quote::before{content:"\201C";position:absolute;left:10px;top:2px;font-size:28px;color:#c8c8c8;font-style:normal}
.author{left:0;top:97px;display:flex;gap:10px;font-family:"PT Sans",sans-serif;font-size:8.5px;line-height:13px;color:#333}
.author i{font-style:normal;color:#777}
.difference{left:412px;top:858px;width:290px;text-align:center}
.difference h2{text-align:left}
.difference p{margin-top:16px;font-family:"PT Sans",sans-serif;font-size:8.5px;line-height:13px;color:#555}
.cta{display:inline-block;margin-top:15px;background:var(--orange);color:#fff;font-family:"PT Sans",sans-serif;font-size:8px;padding:4px 9px;box-shadow:0 0 0 2px #f7d7a8}

/* footer */
.site-footer{left:0;top:1005px;width:782px;height:195px;background:var(--footer);color:var(--footer-text);font-family:"PT Sans",sans-serif}
.footer-curve{left:0;top:-2px}
.footer-brand{left:74px;top:74px;width:125px;font-weight:700;font-size:16px;line-height:17px;color:#fff}
.footer-brand small{display:block;font-size:8px;line-height:11px;font-weight:700}
.col{top:43px;width:150px;font-size:8.5px;line-height:13px}
.col h4{font-weight:400;font-size:10px;margin-bottom:12px;color:#fff}
.col b{color:#fff}
.contact-item{position:relative;padding-left:20px;margin-bottom:8px}
.contact-item svg{position:absolute;left:0;top:1px}
.social{display:flex;gap:8px;margin-top:11px}
.social span{width:14px;height:14px}
.menu li{list-style:none;color:var(--gold);line-height:18.5px}
.menu li::before{content:"›";margin-right:5px}
.to-top{left:746px;top:141px;width:28px;height:28px;border-radius:50%;border:1.5px solid #777;background:#111}
</style>
</head>
<body>

<header class="site-header abs">
  <div class="login abs"><span>Login</span><span class="field"></span><span class="field"></span><span class="go"></span></div>
  <nav class="main-nav abs">
    <span class="current">About us</span><span>Services</span><span>Working with us</span><span>Contact us</span><span>Links</span><span>Testimonials</span><span>News</span>
  </nav>
  <div class="brand abs">
    <span class="brand-mark"></span>
    <div class="brand-name">FENWAY LODGE<small>ADVISORY</small></div>
  </div>
</header>

<section class="hero abs">
  <div class="hero-frame abs">
    <div class="hero-photo abs" role="img" aria-label="Photo of a consultant in a red dress leaning on a railing at a marina"></div>
  </div>
  <div class="hero-arrow prev abs"><svg width="10" height="12"><path d="M2 1l6 5-6 5" fill="none" stroke="#fff" stroke-width="2.5"/></svg></div>
  <div class="hero-arrow next abs"><svg width="10" height="12"><path d="M8 1L2 6l6 5" fill="none" stroke="#fff" stroke-width="2.5"/></svg></div>
</section>

<section class="intro abs">
  <h2>Getting to Fenway Lodge Advisory</h2>
  <p class="lead">Fenway Lodge Advisory aims to service the needs of its clients by focusing on the present rather than</p>
  <p>reporting on historical figures. We recognise that business owners benefit from regular contact with their accountant. One who undertakes a hands on approach in working with business owners to improve their business.</p>
</section>

<section class="why abs">
  <h2>Why Chooes us</h2>
  <div class="why-rule abs"></div>
  <div class="why-pager abs"><span>‹</span><span>›</span></div>
  <div class="post-date abs"><b>20</b><i>Jun</i><i>2013</i></div>
  <div class="post-title abs">Fusce malesuada orci sed euismod pellentesque</div>
  <div class="post-meta abs">Studio Larkfield / 3 Comments</div>
  <p class="post-text abs">Fenway Lodge Advisory aims to service the needs of its clients by focusing on the present rather than reporting on historical figures. We recognise that business...</p>
</section>

<section class="team abs">
  <div class="portrait abs" style="left:68px;top:19px" role="img" aria-label="Portrait of a team member at the marina"></div>
  <div class="badge featured abs" style="left:160px;top:117px"><h3>Here We Are</h3><p>We are located in NYC and Toronto with more offices all over the world.</p></div>
  <div class="portrait abs" style="left:292px;top:19px" role="img" aria-label="Portrait of a team member at the marina"></div>
  <div class="badge abs" style="left:385px;top:114px"><h3>The Team</h3><p>We have a dedicated team to find the best solutions</p></div>
  <div class="portrait abs" style="left:531px;top:21px" role="img" aria-label="Portrait of a team member at the marina"></div>
  <div class="badge abs" style="left:624px;top:116px"><h3>The Team</h3><p>We have a dedicated team to find the best solutions</p></div>
</section>
<div class="dots abs"><span></span><span></span></div>

<section class="tips abs">
  <h2>6 Tips for Naming your Business</h2>
  <blockquote class="quote abs">One of the best service so far. They're fast, accurate and professional. Their support is excellent, they respond within 2 hours. I definitely recommend them for anyone!</blockquote>
  <div class="author abs">
    <svg width="24" height="22"><circle cx="12" cy="7" r="5" fill="#8a8a8a"/><path d="M1 22c0-7 5-9 11-9s11 2 11 9z" fill="#8a8a8a"/></svg>
    <div>Marcus Reed<br><i>CEO of Brightmoor Ltd.</i></div>
  </div>
</section>

<section class="difference abs">
  <h2>Fenway Lodge Advisory Difference</h2>
  <p>Donec faucibus neque leo. Morbi ipsum lacus, pretium vitae tempor lacinia id lacus. Cras vel enim leo. Mauris non blandit ligula. Fusce libero, consectetur a hendrerit sed, aliquet nec nulla.</p>
  <span class="cta">GET A FREE QUOTE!</span>
</section>

<footer class="site-footer abs">
  <svg class="footer-curve abs" width="782" height="20"><path d="M0 0H782V20Q391 -6 0 20Z" fill="#fff"/><path d="M0 18Q391 -6 782 18" fill="none" stroke="#9a9a9a" stroke-width="3"/></svg>
  <div class="footer-brand abs">FENWAY LODGE<small>ADVISORY</small></div>
  <div class="col abs" style="left:215px">
    <h4>ABOUT THE COMPANY</h4>
    <p>We are Halden Ltd. and we create awesome stuff! Look around on our site and figure out why we are the best on the market!</p>
    <div class="social"><span style="background:#3b5b98"></span><span style="background:#2aa4df"></span><span style="background:#444"></span><span style="background:#d21f2e"></span><span style="background:#f06a13"></span></div>
  </div>
  <div class="col abs" style="left:381px">
    <h4>CONTACT INFORMATION</h4>
    <div class="contact-item"><svg width="10" height="12"><path d="M5 0a4 4 0 0 1 4 4c0 3-4 8-4 8S1 7 1 4a4 4 0 0 1 4-4z" fill="#999"/><circle cx="5" cy="4" r="1.5" fill="#1f1f1f"/></svg><b>Address</b><br>Great Lantern Street 78.,<br>New York, USA</div>
    <div class="contact-item"><svg width="12" height="10"><rect x="0" y="0" width="12" height="4" rx="2" fill="#999"/><rect x="2" y="5" width="8" height="5" fill="#999"/></svg><b>Phone</b><br>+42 5355 0198</div>
    <div class="contact-item"><svg width="12" height="9"><rect width="12" height="9" fill="#999"/><path d="M0 0l6 5 6-5" fill="none" stroke="#1f1f1f"/></svg><b>Email</b><br>info@brightharbor.com</div>
  </div>
  <div class="col abs" style="left:548px">
    <h4>IMPORTANT MENU</h4>
    <ul class="menu"><li>Frequently Asked Questions</li><li>About Us</li><li>Contact Page</li><li>Privacy Policy</li><li>Terms of Use</li></ul>
  </div>
  <div class="to-top abs"><svg width="26" height="26"><path d="M7 16l6-6 6 6" fill="none" stroke="#ddd" stroke-width="1.5"/></svg></div>
</footer>

</body>
</html>
```